Business Card Design

We need a business card design for an existing business. Our main trading brand is www.brightmeadowsaver.co.uk

We attach various logo files - please use the version that will produce the sharpest image on the business card.

We are flexible about shape of card etc. Please think outside the box as to what goes on front and what goes on back of the card

We want to be able to amend the card (once the design has been agreed ) to add additional staff details, but the text to go on it will be generic

Details to go on card ( for the first generic one) are fairly minimal as we don't like cluttered business cards:-

Tom Harker
Managing Director

Mobile: 07812 548 207
Email: t.harker@brightmeadowsaver.co.uk

```html
<!DOCTYPE html>
<html lang="en">
<head>
<meta charset="utf-8">
<title>Bright Meadow Saver – Business Card</title>
<link rel="stylesheet" href="https://fonts.googleapis.com/css2?family=Open+Sans:wght@400;600;700&display=swap">
<style>
  :root {
    --canvas-bg: #4a4c4f;
    --card-white: #f7f7f7;
    --card-white-edge: #e6e6e6;
    --card-navy-top: #2c5e7d;
    --card-navy-bottom: #1c455f;
    --brand-blue: #2f94d2;
    --brand-light: #5fb0e0;
    --text-grey: #555a5e;
    --text-dark: #3d4246;
    --icon-cut: #f0f0f0;
  }
  * { box-sizing: border-box; margin: 0; padding: 0; }
  html, body {
    width: 1200px;
    height: 900px;
    overflow: hidden;
    background: var(--canvas-bg);
    font-family: "Open Sans", Arial, sans-serif;
  }
  .canvas {
    position: relative;
    width: 1200px;
    height: 900px;
  }
  .card {
    position: absolute;
    width: 620px;
    height: 360px;
    border-radius: 3px;
    overflow: hidden;
    box-shadow: 0 10px 28px rgba(0, 0, 0, 0.35);
  }
  .card-back {
    left: 340px;
    top: 60px;
    background: linear-gradient(160deg, var(--card-navy-top), var(--card-navy-bottom));
  }
  .card-front {
    left: 240px;
    top: 480px;
    background: linear-gradient(180deg, var(--card-white), var(--card-white-edge));
  }
  .brand-name {
    position: absolute;
    font-weight: 400;
    letter-spacing: 0.2px;
    white-space: nowrap;
  }
  .card-back .brand-name {
    right: 40px;
    bottom: 70px;
    font-size: 26px;
    color: var(--brand-light);
  }
  .card-front .brand-name {
    left: 36px;
    top: 78px;
    font-size: 30px;
    color: var(--brand-blue);
  }
  .contact {
    position: absolute;
    left: 268px;
    right: 30px;
    top: 206px;
    color: var(--text-grey);
  }
  .contact-name {
    font-size: 22px;
    font-weight: 700;
    color: var(--brand-blue);
    line-height: 1.2;
  }
  .contact-role {
    font-size: 16px;
    line-height: 1.4;
    margin-bottom: 6px;
  }
  .contact-line {
    display: flex;
    align-items: center;
    gap: 8px;
    font-size: 16px;
    line-height: 1.6;
    color: var(--text-dark);
    white-space: nowrap;
  }
  .contact-line svg {
    width: 16px;
    height: 16px;
    fill: var(--brand-blue);
    flex: none;
  }
</style>
</head>
<body>
<main class="canvas">
  <section class="card card-back" aria-label="Card back">
    <p class="brand-name">brightmeadowsaver.co.uk</p>
  </section>

  <section class="card card-front" aria-label="Card front">
    <p class="brand-name">brightmeadowsaver.co.uk</p>
    <div class="contact">
      <p class="contact-name">Tom Harker</p>
      <p class="contact-role">Managing Director</p>
      <p class="contact-line">
        <svg viewBox="0 0 24 24" aria-hidden="true"><path d="M6.6 10.8a15.1 15.1 0 0 0 6.6 6.6l2.2-2.2a1 1 0 0 1 1-.25 11.4 11.4 0 0 0 3.6.57 1 1 0 0 1 1 1V20a1 1 0 0 1-1 1A17 17 0 0 1 3 4a1 1 0 0 1 1-1h3.5a1 1 0 0 1 1 1c0 1.25.2 2.45.57 3.57a1 1 0 0 1-.25 1z"/></svg>
        07812 548 207
      </p>
      <p class="contact-line">
        <svg viewBox="0 0 24 24" aria-hidden="true"><rect x="2" y="5" width="20" height="14" rx="1"/><path d="M2.5 6 12 13.2 21.5 6" fill="none" stroke="var(--icon-cut)" stroke-width="1.6"/></svg>
        t.harker@brightmeadowsaver.co.uk
      </p>
    </div>
  </section>
</main>
</body>
</html>
```